Business Card Design

We Import cars and commercial vehicles, we have been in business around 12 years, we are based in Christchurch, New Zealand.
I really like the web address on card, possibly right along the bottom of the card?
We specialize in commercial vans, maybe worth a mention?
The logo has the name in it so probably don't need to have twice?

I really like a clean smart look, not too cluttered

Industry/Entity Type

Business

Contact Information for Business Card

DLQ NIPPON MOTORS, Garth Whitmore, Managing Director
web address: www.dlqnippon.example
cell phone. 021 584 217

Requirements
Must have
• the logo, and all the contact details.

Forgot to add my email address, garth@dlqnippon.example
Nice to have
• Just thinking as the card is looking a little empty maybe somewhere written what we do? 'Specializing in commercial vans'
Not sure but we import Japanese vehicles, possibly adding some brands like Velkora Parvex Quillo Rundel etc? Not sure on that one.

```html
<!DOCTYPE html>
<html lang="en">
<head>
<meta charset="utf-8">
<title>DLQ Nippon Motors – Business Card</title>
<link href="https://fonts.googleapis.com/css2?family=Mulish:wght@400;600;700;900&display=swap" rel="stylesheet">
<style>
  :root {
    --bg: #d9d6d1;
    --card-black: #111111;
    --card-black-hi: #2a2a2a;
    --silver-light: #f2f2f2;
    --silver-mid: #bdbdbd;
    --silver-dark: #8c8c8c;
    --ink: #1a1a1a;
    --ink-soft: #555555;
    --white: #ffffff;
    --brand-red: #d2151f;
    --brand-grey: #7a7a7a;
  }
  * { margin: 0; padding: 0; box-sizing: border-box; }
  html, body { width: 1200px; height: 871px; overflow: hidden; }
  body {
    background: var(--bg);
    font-family: "Mulish", "Century Gothic", sans-serif;
    position: relative;
  }
  .card {
    position: absolute;
    width: 600px;
    height: 343px;
    border-radius: 4px;
    overflow: hidden;
    box-shadow: 0 14px 30px rgba(0,0,0,.28);
  }

  /* Front */
  .card-front {
    left: 60px; top: 60px;
    background: linear-gradient(160deg, var(--card-black-hi) 0%, var(--card-black) 55%);
  }
  .front-logo {
    position: absolute; left: 120px; top: 62px;
    display: flex; align-items: center; gap: 18px;
  }
  .front-logo .wordmark {
    font-weight: 900; font-size: 44px; line-height: .95;
    color: var(--silver-light); letter-spacing: 1px;
  }
  .logo-dot {
    width: 22px; height: 22px; border-radius: 50%;
    background: var(--silver-mid);
  }
  .front-band {
    position: absolute; left: 0; right: 0; top: 196px; height: 62px;
    background: linear-gradient(180deg, var(--silver-light) 0%, var(--silver-mid) 100%);
    display: flex; align-items: center; justify-content: center;
  }
  .front-band .tagline {
    font-weight: 700; font-size: 26px; color: var(--ink); letter-spacing: .3px;
  }

  /* Back */
  .card-back {
    left: 540px; top: 468px;
    background: linear-gradient(180deg, var(--white) 0%, #f1f1f1 100%);
  }
  .back-logo {
    position: absolute; left: 40px; top: 26px;
    display: flex; align-items: center; gap: 14px;
  }
  .back-logo .wordmark {
    font-weight: 900; font-size: 34px; line-height: .95; color: var(--ink);
  }
  .back-logo .logo-dot { background: var(--ink); width: 18px; height: 18px; }
  .person { position: absolute; left: 40px; top: 128px; }
  .person .name { font-weight: 700; font-size: 18px; color: var(--ink); }
  .person .role { font-size: 13px; color: var(--ink-soft); margin-top: 3px; }
  .contacts { position: absolute; left: 40px; top: 188px; list-style: none; }
  .contacts li {
    display: flex; align-items: center; gap: 12px;
    font-size: 14px; color: var(--ink-soft); height: 22px;
  }
  .contacts svg { width: 14px; height: 14px; fill: none; stroke: var(--ink); stroke-width: 1.4; }
  .brands {
    position: absolute; right: 30px; top: 236px;
    display: flex; gap: 26px; align-items: center;
  }
  .brand { display: flex; flex-direction: column; align-items: center; gap: 4px; font-weight: 700; font-size: 11px; }
  .brand .mark { width: 22px; height: 22px; border-radius: 50%; border: 2px solid currentColor; }
  .brand-parvex { color: var(--brand-grey); }
  .brand-velkora { color: var(--brand-red); }
  .brand-rundel { color: var(--brand-red); }
  .back-footer { position: absolute; left: 0; bottom: 0; width: 600px; height: 80px; }
  .website {
    position: absolute; right: 34px; bottom: 14px;
    font-size: 16px; color: var(--ink-soft); letter-spacing: .4px;
  }
</style>
</head>
<body>

<section class="card card-front">
  <div class="front-logo">
    <div class="wordmark">DLQ NIPPON<br>MOTORS</div>
    <span class="logo-dot"></span>
  </div>
  <div class="front-band">
    <p class="tagline">Specializing in commercial vans</p>
  </div>
</section>

<section class="card card-back">
  <div class="back-logo">
    <div class="wordmark">DLQ NIPPON<br>MOTORS</div>
    <span class="logo-dot"></span>
  </div>

  <div class="person">
    <p class="name">Garth Whitmore</p>
    <p class="role">Managing Director</p>
  </div>

  <ul class="contacts">
    <li>
      <svg viewBox="0 0 14 14"><rect x="1" y="3" width="12" height="8"/><polyline points="1,3 7,8 13,3"/></svg>
      garth@dlqnippon.example
    </li>
    <li>
      <svg viewBox="0 0 14 14"><path d="M2 5 Q7 1 12 5 L11 7 L9 6 L9 5 Q7 4 5 5 L5 6 L3 7 Z"/><rect x="3" y="8" width="8" height="5"/></svg>
      021 584 217
    </li>
    <li>
      <svg viewBox="0 0 14 14"><rect x="4" y="1" width="6" height="12" rx="1"/><line x1="6" y1="11" x2="8" y2="11"/></svg>
      021 584 217
    </li>
  </ul>

  <div class="brands">
    <div class="brand brand-parvex"><span class="mark"></span>PARVEX</div>
    <div class="brand brand-velkora"><span class="mark"></span>VELKORA</div>
    <div class="brand brand-rundel"><span class="mark"></span>RUNDEL</div>
  </div>

  <svg class="back-footer" viewBox="0 0 600 80" preserveAspectRatio="none" aria-hidden="true">
    <defs>
      <linearGradient id="footer-silver" x1="0" y1="0" x2="0" y2="1">
        <stop offset="0" stop-color="#e6e6e6"/>
        <stop offset="1" stop-color="#c4c4c4"/>
      </linearGradient>
    </defs>
    <polygon points="0,18 330,18 355,44 600,44 600,80 0,80" fill="url(#footer-silver)"/>
    <polyline points="0,18 330,18 355,44 600,44" fill="none" stroke="#9a9a9a" stroke-width="1.5"/>
  </svg>
  <p class="website">www.dlqnippon.example</p>
</section>

</body>
</html>
```